Pillow Company needs Pillow Insert Design

I just started a new pillow line with two pillow types. I have a hotel pillow and an organic pillow. I need two pillow insert signs designed that follow the same layout but are different color types. I want one sign to incorporate silver and white look and another sign to incorporate a green and white look (this one to look organic). They must have the same layout but different colors. I have include examples of what I want it to look like. In addition, I have uploaded the two hi res images for each sign. My logo is uploaded too.

I am open to other concepts and colors as long as it looks modern, clean and upscale. In addition, I need a Made in the USA logo on the pillow insert designs.

I have attached details on sign, images to be used, and examples that I like.

The Pillow Sign Size is 12 inches x 12 inches.

```html
<!DOCTYPE html>
<html lang="en">
<head>
<meta charset="utf-8">
<title>LullaNest Pillow Insert Signs</title>
<link href="https://fonts.googleapis.com/css2?family=Arimo:wght@400;700&family=Roboto:wght@300;400&display=swap" rel="stylesheet">
<style>
  :root {
    --page-bg: #ffffff;
    --card-bg: #ffffff;
    --card-border: #c9c9c9;
    --brand-green: #3fa649;
    --ink: #1a1a1a;
    --body-ink: #3a3a3a;
    --silver-accent: #87a0bf;
    --organic-accent: #75875d;
    --badge-red: #c8242f;
    --badge-blue: #23408f;
  }
  * { box-sizing: border-box; margin: 0; padding: 0; }
  html, body {
    width: 1200px; height: 1000px; overflow: hidden;
    background: var(--page-bg);
    font-family: "Arimo", Arial, sans-serif;
  }
  .canvas { position: relative; width: 1200px; height: 1000px; }

  .sign {
    position: absolute;
    width: 531px; height: 531px;
    background: var(--card-bg);
    border: 1px solid var(--card-border);
    overflow: hidden;
  }
  .sign--hotel { left: 57px; top: 138px; --accent: var(--silver-accent); }
  .sign--organic { left: 612px; top: 330px; --accent: var(--organic-accent); }

  .sign__photo {
    position: absolute; left: 0; top: 190px; width: 100%; height: 230px;
  }
  .sign--hotel .sign__photo {
    background: linear-gradient(180deg, #e4e2df 0%, #d9cfc4 30%, #ece9e6 65%, #ffffff 100%);
  }
  .sign--organic .sign__photo {
    background: linear-gradient(180deg, #e2e4e2 0%, #d6c8bc 35%, #eceaea 70%, #ffffff 100%);
  }

  .brand {
    position: absolute; left: 17px; top: 18px;
    display: flex; align-items: center; gap: 12px;
  }
  .brand__mark { width: 54px; height: 46px; background: var(--brand-green); }
  .brand__name { font-size: 24px; font-weight: 700; color: var(--brand-green); letter-spacing: -0.2px; }

  .tagline {
    position: absolute; left: 17px; top: 72px;
    font-size: 16.5px; line-height: 19px; font-weight: 400;
    color: var(--ink); letter-spacing: 0.2px;
  }
  .intro {
    position: absolute; left: 17px; top: 125px; width: 266px;
    font-size: 9.6px; line-height: 11px; color: var(--body-ink);
  }

  .product-panel {
    position: absolute; right: 0; top: 0; width: 231px; height: 194px;
    background: var(--accent); color: #fff; text-align: right;
    padding: 12px 17px 0 6px;
  }
  .product-panel__title {
    font-family: "Roboto", Arial, sans-serif; font-weight: 300;
    font-size: 37px; line-height: 47px; white-space: nowrap;
    letter-spacing: -0.3px;
  }
  .product-panel__lede {
    margin-top: 14px;
    font-family: "Roboto", Arial, sans-serif; font-weight: 300;
    font-size: 15.5px; line-height: 19px;
  }

  .features-heading {
    position: absolute; left: 8px; top: 406px;
    background: var(--accent); color: #fff;
    font-weight: 700; font-size: 12.5px; letter-spacing: 0.2px;
    padding: 3px 8px;
  }
  .features {
    position: absolute; left: 17px; top: 433px;
    list-style: none;
    font-size: 8.6px; line-height: 10.4px; color: var(--body-ink);
  }
  .features li::before { content: "• "; }
  .features .indent { padding-left: 7px; }
  .features .indent::before { content: ""; }

  .origin-badge {
    position: absolute; right: 17px; top: 443px; width: 62px; text-align: center;
  }
  .origin-badge__shape { display: block; width: 62px; height: 36px; }
  .origin-badge__label { font-size: 8.4px; font-weight: 700; color: var(--ink); margin-top: 2px; }

  .sign-footer {
    position: absolute; right: 17px; top: 493px; text-align: right;
    font-size: 8.8px; line-height: 10.6px; color: var(--body-ink);
  }
</style>
</head>
<body>
<main class="canvas">

  <section class="sign sign--hotel">
    <div class="sign__photo" role="img" aria-label="Smiling family of three lying together in a bed with white pillows and duvet"></div>
    <div class="brand"><span class="brand__mark"></span><span class="brand__name">LullaNest</span></div>
    <h2 class="tagline">SURROUND YOURSELF<br>WITH THE BEST!</h2>
    <p class="intro">We added revolutionary features from our advanced Super Soft Premium Memory Foam that has an open cell structure design that recovers quickly and does not trap heat to our gel infused polyester fiber to our temperature managing Lyoweave Fabric.</p>
    <div class="product-panel">
      <h1 class="product-panel__title">luxurious<br>pillow</h1>
      <p class="product-panel__lede">Especially designed to give you the most comfortable night's sleep in your life.</p>
    </div>
    <h3 class="features-heading">DESIGNED FOR ALL TYPES OF SLEEP POSITIONS.</h3>
    <ul class="features">
      <li>Made From the Finest Premium Materials</li>
      <li>Adjusts to your Body Weight and Temperature</li>
      <li>Ventilated and Does Not Trap Heat</li>
      <li>Cool Non-Allergenic, Anti-Microbial, and Hypoallergenic</li>
      <li>Conforms to Head and Neck for optimal Alignment</li>
      <li class="indent">during sleep</li>
      <li>Mildew Proof and Dust Mite Resistant</li>
      <li>PureFoam-US ® toxin free certified foam</li>
    </ul>
    <div class="origin-badge">
      <svg class="origin-badge__shape" viewBox="0 0 62 36" aria-hidden="true"><rect width="62" height="36" fill="var(--badge-red)"/><rect width="24" height="18" fill="var(--badge-blue)"/></svg>
      <div class="origin-badge__label">Made in USA</div>
    </div>
    <p class="sign-footer">Surround Yourself with the Best!<br>Individually Handcrafted and Made in USA</p>
  </section>

  <section class="sign sign--organic">
    <div class="sign__photo" role="img" aria-label="Couple lying face to face in a bright bedroom with white bedding"></div>
    <div class="brand"><span class="brand__mark"></span><span class="brand__name">LullaNest</span></div>
    <h2 class="tagline">SURROUND YOURSELF<br>WITH THE BEST!</h2>
    <p class="intro">We added revolutionary features from our advanced Super Soft Premium Memory Foam that has an open cell structure design that recovers quickly and does not trap heat to our gel infused polyester fiber to our temperature managing Lyoweave Fabric.</p>
    <div class="product-panel">
      <h1 class="product-panel__title">alternative<br>down pillow</h1>
      <p class="product-panel__lede">Especially designed to give you the most comfortable night's sleep in your life.</p>
    </div>
    <h3 class="features-heading">DESIGNED FOR ALL TYPES OF SLEEP POSITIONS.</h3>
    <ul class="features">
      <li>Made From the Finest Premium Materials</li>
      <li>Adjusts to your Body Weight and Temperature</li>
      <li>100% Certified Organic Cotton Fabric</li>
      <li>Cool Non-Allergenic, Anti-Microbial, and Hypoallergenic</li>
      <li>Conforms to Head and Neck for optimal Alignment</li>
      <li class="indent">during sleep</li>
      <li>Mildew Proof and Dust Mite Resistant</li>
      <li>PureFoam-US ® toxin free certified foam</li>
    </ul>
    <div class="origin-badge">
      <svg class="origin-badge__shape" viewBox="0 0 62 36" aria-hidden="true"><rect width="62" height="36" fill="var(--badge-red)"/><rect width="24" height="18" fill="var(--badge-blue)"/></svg>
      <div class="origin-badge__label">Made in USA</div>
    </div>
    <p class="sign-footer">Surround Yourself with the Best!<br>Individually Handcrafted and Made in USA</p>
  </section>

</main>
</body>
</html>
```